MYLAR BAG FOR FIZZLE

Ive included a template for the design provided by the printer.

FRONT :
I'd like to match the box , i have a screenshot. I used an app to create it and the box printer somehow applied it. The app tells me the fonts, let me know if you would like the font names.

BACK SIDE :

DIRECTIONS FOR USE : THC TOLERANCE MAY VARY FROM PERSON TO PERSON. THE ACCEPTED RECOMMENDATION FOR A NEW USER IS 10 MG THC. REFERENCE THE AFFIXED VANTOL TAG FOR ACCURATE DOSAGE INFORMATION .

INGREDIENTS : RICE, SUGAR, THC EXTRACT, COCONUT OIL, ARTIFICIAL FLAVOR & COLOR, SALT, MALT SYRUP

ALLERGEN WARNING : CONTAINS COCONUT.
MADE IN A FACULTY THAT HANDLES PEANUTS AND OTHER TREE NUTS.

THE ACTUAL VALUE OF REPORTED CANNABINOIDS MAY VARY FROM THE REPORTED VALUE BY +/-10 %

ACTIVATION TIME :10-60 MIN

WARNING : FOR USE BY INDIVIDUALS 21 YRS OF AGE OR OLDER OR BY REGISTERED QUALIFYING PATIENTS ONLY. IT IS ILLEGAL TO DRIVE A MOTOR VEHICLE WHILE UNDER THE INFLUENCE OF MARIJUANA.

KEEP OUT OF REACH OF CHILDREN.

FEDERAL TOXIN RESPONSE BUREAU
1 800 555 0147

WARNING : USE BY PREGNANT OR BREASTFEEDING WOMEN OR BY WOMEN WHO PLAN TO BECOME
PREGNANT MAY RESULT IN FETAL INJURY, PRETERM BIRTH, LOW BIRTHWEIGHT, OR DEVELOPMENTAL
PROBLEMS FOR THE CHILD.

MADE IN A MARIJUANA FACILITY

MADE & DISTRIBUTED BY MARGOT'S HAZE COMPANY
LICENSE # KX T 004837
(LOGO)
www.HAZEBITES.INFO

• CMKY colors

```html
<!DOCTYPE html>
<html lang="en">
<head>
<meta charset="utf-8">
<title>Haze Bites – THC Cereal Mylar Bag</title>
<link rel="stylesheet" href="https://fonts.googleapis.com/css2?family=Bowlby+One&family=Montserrat:wght@500;600;700&display=swap">
<style>
  :root {
    --bag-pink: #e8b0d2;
    --cream-yellow: #f0edaa;
    --white: #ffffff;
    --ink: #222222;
    --badge-green: #1f7a3c;
    --page: #ffffff;
  }
  * { margin: 0; padding: 0; box-sizing: border-box; }
  html, body { width: 1200px; height: 1067px; overflow: hidden; background: var(--page); }
  .canvas { position: relative; width: 1200px; height: 1067px; }

  .bag-face {
    position: absolute; top: 171px; width: 461px; height: 737px;
    background: var(--bag-pink); border-radius: 4px;
  }
  .bag-front { left: 127px; }
  .bag-back { left: 631px; }

  .seal-line {
    position: absolute; left: 32px; right: 32px; height: 2px;
    background: rgba(255,255,255,0.35);
  }

  .display { font-family: "Bowlby One", "Arial Black", sans-serif; line-height: 1; text-align: center; position: absolute; left: 0; width: 100%; }
  .white { color: var(--white); }
  .yellow { color: var(--cream-yellow); }

  .adult-use { top: 145px; font-size: 25px; }
  .title-thc { top: 175px; font-size: 72px; letter-spacing: -1px; }
  .title-cereal { top: 255px; font-size: 70px; letter-spacing: -1px; }
  .flavor-frosted { top: 370px; font-size: 64px; letter-spacing: -1px; }
  .flavor-strawberry { top: 434px; font-size: 42px; letter-spacing: -1px; }
  .flavor-fizzle { top: 480px; font-size: 44px; }

  .tagline {
    position: absolute; left: 0; width: 100%; top: 537px; text-align: center;
    font-family: "Montserrat", sans-serif; font-weight: 600; font-size: 15px;
    letter-spacing: 4px; line-height: 19px; color: var(--white);
  }
  .brand-name {
    position: absolute; font-family: "Montserrat", sans-serif; font-weight: 700;
    color: var(--cream-yellow); line-height: 1; white-space: nowrap;
  }
  .front-brand { left: 0; width: 100%; top: 612px; text-align: center; font-size: 42px; }
  .child-warning {
    position: absolute; left: 0; width: 100%; top: 682px; text-align: center;
    font-family: "Montserrat", sans-serif; font-weight: 600; font-size: 14px;
    letter-spacing: 3.5px; color: var(--white);
  }
  .regulatory-badge {
    position: absolute; left: 352px; top: 148px; width: 60px; height: 60px;
    border-radius: 50%; background: var(--badge-green);
  }

  .back-brand { left: 67px; top: 172px; font-size: 46px; }
  .info-panel {
    position: absolute; left: 63px; top: 251px; width: 337px; height: 228px;
    background: var(--cream-yellow); border-radius: 12px; padding: 11px 12px;
    font-family: "Montserrat", sans-serif; font-weight: 500; font-size: 10px; line-height: 13.5px;
    color: var(--ink); text-transform: uppercase;
  }
  .info-panel p { margin-bottom: 13px; }
  .info-panel strong, .warning-panel strong { font-weight: 700; }
  .warning-panel {
    position: absolute; left: 70px; top: 489px; width: 323px; height: 117px;
    background: var(--white); padding: 6px 6px;
    font-family: "Montserrat", sans-serif; font-weight: 500; font-size: 7px; line-height: 9.6px;
    color: var(--ink); text-transform: uppercase;
  }
  .warning-panel p { margin-bottom: 6px; }
  .warning-label { font-size: 8px; }
  .hotline { text-align: center; font-weight: 700; font-size: 8px; margin: 0; }
  .hotline span { margin-left: 10px; }
  .facility-note {
    position: absolute; left: 0; width: 100%; top: 625px; text-align: center;
    font-family: "Montserrat", sans-serif; font-weight: 700; font-size: 8.5px;
    color: var(--cream-yellow); letter-spacing: 0.3px;
  }
  .footer-brand { left: 82px; top: 666px; font-size: 21px; }
  .distributor {
    position: absolute; left: 226px; top: 650px;
    font-family: "Montserrat", sans-serif; font-weight: 700; font-size: 8.5px; line-height: 13px;
    color: var(--cream-yellow); text-transform: uppercase; letter-spacing: 0.2px;
  }
</style>
</head>
<body>
<main class="canvas">

  <section class="bag-face bag-front" aria-label="Front of bag">
    <div class="seal-line" style="top:88px"></div>
    <div class="seal-line" style="top:98px"></div>

    <div class="display white adult-use" style="left:-20px">ADULT - USE</div>
    <div class="display white title-thc" style="left:-20px">THC</div>
    <div class="display yellow title-cereal">CEREAL</div>

    <div class="regulatory-badge" aria-hidden="true"></div>

    <div class="display white flavor-frosted">FROSTED</div>
    <div class="display white flavor-strawberry">STRAWBERRY</div>
    <div class="display white flavor-fizzle">FIZZLE</div>

    <p class="tagline">FROSTED STRAWBERRY<br>CEREAL ENHANCED WITH THC</p>

    <div class="brand-name front-brand">HAZE BITES</div>

    <p class="child-warning">KEEP OUT OF REACH OF CHILDREN</p>
  </section>

  <section class="bag-face bag-back" aria-label="Back of bag">
    <div class="seal-line" style="top:88px"></div>
    <div class="seal-line" style="top:98px"></div>

    <div class="brand-name back-brand">HAZE BITES</div>

    <div class="info-panel">
      <p><strong>Directions for use :</strong> THC tolerance may vary from person to person. The accepted recommendation for a new user is 10 mg THC. Reference the affixed VANTOL tag for accurate dosage information.</p>
      <p><strong>Ingredients :</strong> Rice, sugar, THC extract, coconut oil, artificial flavor &amp; color, salt, malt syrup</p>
      <p><strong>Allergen warning :</strong> Contains coconut.<br>Made in a faculty that handles peanuts and other tree nuts.</p>
      <p>The actual value of reported cannabinoids may vary from the reported value by +/-10 %</p>
      <p><strong>Activation time :</strong> 10-60 min</p>
    </div>

    <div class="warning-panel">
      <p><strong class="warning-label">Warning :</strong><br>For use by individuals 21 yrs of age or older or by registered qualifying patients only. It is illegal to drive a motor vehicle while under the influence of marijuana. Keep out of reach of children.</p>
      <p>Use by pregnant or breastfeeding women or by women who plan to become pregnant may result in fetal injury, preterm birth, low birthweight, or developmental problems for the child.</p>
      <p class="hotline">FEDERAL TOXIN RESPONSE BUREAU<span>1 800 555 0147</span></p>
    </div>

    <p class="facility-note">MADE IN A MARIJUANA FACILITY</p>

    <div class="brand-name footer-brand">HAZE BITES</div>

    <p class="distributor">Made &amp; distributed by<br>Margot's Haze Company<br>License # KX T 004837<br><span style="text-transform:none">www.HAZEBITES.INFO</span></p>
  </section>

</main>
</body>
</html>
```